Adult Residential Care Provider (Assisted Living) needs a brochure design.

We need a brochure designed for our assisted living facilites in Metairie (adjacent to New Orleans) called Willowmere Elder Homes. We provide adults, typically Seniors, a place to live where they receive 24-hour care/support of their daily living activities, including laundering, cooking, cleaning, grooming, bathing, etc.. I'd like to use our logo and the color choices should be soft and convey comfort. I would also like the brochure to be editable by my administration to make any changes in the future.

```html
<!DOCTYPE html>
<html lang="en">
<head>
<meta charset="utf-8">
<title>Willowmere Elder Homes – Trifold Brochure</title>
<link rel="stylesheet" href="https://fonts.googleapis.com/css2?family=Crimson+Text:wght@400;600&family=Source+Sans+3:wght@400;600&display=swap">
<style>
  :root {
    --backdrop: #666666;
    --cream: #efe7d6;
    --cream-light: #f5efe2;
    --teal-dark: #0f4a43;
    --teal-text: #1d4b43;
    --sage: #86a597;
    --sage-light: #a9c1b5;
    --taupe: #6f6b5c;
    --ink: #3b3a34;
    --pill: #e9dccb;
    --white: #ffffff;
  }
  * { box-sizing: border-box; margin: 0; padding: 0; }
  html, body { width: 860px; height: 1200px; overflow: hidden; }
  body { background: var(--backdrop); font-family: "Source Sans 3", Arial, sans-serif; color: var(--ink); position: relative; }

  .sheet { position: absolute; left: 60px; width: 740px; height: 575px; display: grid; grid-template-columns: 1fr 1fr 1fr; box-shadow: 0 4px 10px rgba(0,0,0,.45); }
  .sheet--outside { top: 17px; }
  .sheet--inside { top: 608px; }

  .panel { position: relative; overflow: hidden; background: var(--cream); }
  .panel--sage { background: var(--sage); }
  .panel > * { position: absolute; }
  .curve { left: 0; top: 0; width: 100%; height: 100%; }

  .photo { background: linear-gradient(135deg, #d9cbb8, #a9a08c); }
  .photo--warm { background: linear-gradient(135deg, #e8d6c2 0%, #c9b59b 50%, #8d8a70 100%); }
  .photo--green { background: linear-gradient(160deg, #8fa46e 0%, #c7b79a 45%, #5a6a7a 100%); }
  .photo--room { background: linear-gradient(135deg, #e6e4dc, #b8c0b4); }
  .photo--portrait { border-radius: 50%; background: radial-gradient(circle at 50% 40%, #cfc3b3, #5b5148); border: 5px solid var(--taupe); }
  .photo--circle { border-radius: 50%; border: 3px solid #e8e6e0; }

  .heading { font-family: "Crimson Text", Georgia, serif; font-weight: 400; color: var(--teal-text); font-size: 22px; line-height: 1; }
  .heading--rule { border-bottom: 1px solid var(--teal-text); padding-bottom: 2px; }
  .kicker { font-size: 7px; color: var(--ink); text-transform: uppercase; letter-spacing: -.1px; }
  .body-copy { font-size: 7px; line-height: 1.33; text-align: justify; color: var(--ink); }
  .body-copy p + p { margin-top: 8px; }

  .brand { font-family: "Crimson Text", Georgia, serif; font-weight: 400; color: var(--teal-text); text-align: center; text-transform: uppercase; line-height: 1; }
  .brand__name { display: block; font-size: 24px; letter-spacing: 2.5px; }
  .brand__sub { display: block; font-size: 10.5px; letter-spacing: 2.3px; margin-top: 2px; }

  .center { left: 0; width: 100%; text-align: center; }
  .serif-line { font-family: "Crimson Text", Georgia, serif; }

  .phone-pill { display: inline-flex; align-items: center; gap: 6px; background: var(--teal-dark); color: var(--white); font-size: 12.5px; font-weight: 600; padding: 1px 12px 1px 2px; border-radius: 10px; }
  .phone-pill svg { width: 17px; height: 17px; }
  .url { font-family: "Crimson Text", Georgia, serif; font-size: 13px; color: var(--teal-text); }

  .list { list-style: none; font-size: 7.6px; color: var(--teal-text); }
  .list li { position: relative; padding-left: 12px; height: 17px; line-height: 10px; }
  .list li::before { content: ""; position: absolute; left: 0; top: 2px; width: 6px; height: 6px; border-radius: 50%; background: var(--sage); box-shadow: 0 0 0 1px var(--cream), 0 0 0 2px var(--sage); }
  .panel--sage .list { color: var(--white); }
  .panel--sage .list li::before { background: #d9e4de; box-shadow: 0 0 0 1px var(--sage), 0 0 0 2px #d9e4de; }

  .service { left: 12px; width: 222px; }
  .service h3 { font-family: "Crimson Text", Georgia, serif; font-weight: 400; font-size: 11.5px; color: var(--teal-text); line-height: 1.1; }
  .service p { font-size: 7px; line-height: 1.3; text-align: justify; margin-top: 1px; }
  .service p + p { margin-top: 8px; }
</style>
</head>
<body>

<!-- Outside spread -->
<section class="sheet sheet--outside" aria-label="Brochure outside">

  <article class="panel panel--about">
    <div class="photo photo--warm" role="img" aria-label="Close-up of a caregiver's hand resting on an elderly hand" style="left:0;top:0;width:100%;height:140px;"></div>
    <svg class="curve" viewBox="0 0 247 575" preserveAspectRatio="none" aria-hidden="true">
      <path d="M0 120 C60 95 150 95 247 120 L247 0 L247 575 L0 575 Z" fill="var(--cream)"/>
      <path d="M0 112 C70 90 150 92 247 112 L247 122 C150 100 70 100 0 128 Z" fill="var(--sage)"/>
      <path d="M0 462 C80 455 170 440 247 448 L247 575 L0 575 Z" fill="var(--sage-light)"/>
    </svg>
    <div class="photo photo--portrait" role="img" aria-label="Vintage portrait of the first resident" style="left:126px;top:60px;width:100px;height:100px;"></div>
    <h2 class="heading" style="left:15px;top:145px;">About Us</h2>
    <p class="kicker" style="left:15px;top:178px;">It all started with Margaret</p>
    <div class="body-copy" style="left:15px;top:198px;width:215px;">
      <p>Carol Thibodeaux, RN and home health nurse, needed a place for her mother-in-law, Margaret Thibodeaux, to assist in daily living activities. Carol and her husband Robert realized that with Carol's experience, they could create that exact place that they have been looking for - a warm, family-feel, in a safe environment, that encouraged independence. In 2008, they opened the first location - Birchwood; their first resident, Margaret.</p>
      <p>The word quickly spread to friends, family, and other locals, that Willowmere Elder Homes is a great place for loved ones to be cared for with around-the-clock care. With a growing waiting list, Carol and Rob built the second location, Larkspur, in 2011.</p>
      <p>The love and care that was provided to the residents 14 years ago is growing and remains the core of our philosophy. With more than 20 personal caregivers, we will be caring for yours and our loved one for years to come.</p>
      <p>She is now bringing that love &amp; enthusiasm to the residents at Willowmere Elder Homes where she is just happy to see the smiles on their faces as they participate in her weekly visits.</p>
    </div>
    <div class="photo photo--room" role="img" aria-label="Caregiver sharing tea with an elderly man in an armchair" style="left:0;top:455px;width:100%;height:120px;"></div>
  </article>

  <article class="panel panel--contact">
    <div class="photo photo--warm" role="img" aria-label="Smiling caregiver embracing an elderly woman" style="left:0;top:0;width:100%;height:135px;"></div>
    <svg class="curve" viewBox="0 0 247 575" preserveAspectRatio="none" aria-hidden="true">
      <path d="M0 128 C80 110 160 115 247 100 L247 575 L0 575 Z" fill="var(--cream)"/>
      <path d="M0 122 C80 104 160 108 247 92 L247 100 C160 115 80 110 0 130 Z" fill="var(--sage)"/>
      <path d="M0 470 C90 478 170 470 247 440 L247 575 L0 575 Z" fill="var(--teal-dark)"/>
    </svg>
    <div class="brand center" style="top:196px;"><span class="brand__name">Willowmere</span><span class="brand__sub">Elder Homes</span></div>
    <p class="center serif-line" style="top:254px;font-size:7.5px;color:var(--teal-text);font-weight:600;">Family Owned and Operated Est. 2008</p>
    <h2 class="center serif-line" style="top:290px;font-size:16px;font-weight:600;color:var(--teal-text);letter-spacing:.5px;">CONTACT US</h2>
    <p class="center" style="top:319px;font-size:11px;color:var(--teal-text);">412 Larkspur Ave. Metairie, LA 70005</p>
    <p class="center" style="top:345px;font-size:11px;line-height:1.2;color:var(--teal-text);">2871 Birchwood St.<br>Metairie, LA 70002</p>
    <div class="center" style="top:387px;">
      <span class="phone-pill"><svg viewBox="0 0 20 20" aria-hidden="true"><circle cx="10" cy="10" r="9.5" fill="#e9e6dc"/><circle cx="10" cy="10" r="7.5" fill="var(--teal-dark)"/><path d="M7 5.5 L8.6 5.3 L9.3 7.8 L8.2 8.6 C8.7 9.9 9.9 11.1 11.3 11.7 L12.1 10.6 L14.6 11.3 L14.4 12.9 C11 13.5 6.5 9 7 5.5 Z" fill="#fff"/></svg>(504) 555-0148</span>
    </div>
    <p class="center url" style="top:416px;">www.willowmerehomes.com</p>
    <p class="center serif-line" style="top:493px;font-size:13px;color:#d9d0b8;">Willowmere Elder Homes</p>
    <p class="center" style="top:530px;font-size:7px;line-height:1.4;color:var(--white);">Please contact us at <b>(504) 555-0148</b> or e-mail us<br>at <b>joan.ellison@willowmerehomes.com</b> for more<br>information on getting started.</p>
  </article>

  <article class="panel panel--cover">
    <div class="brand" style="left:0;width:100%;top:26px;"><span class="brand__name" style="font-size:23px;">Willowmere</span><span class="brand__sub">Elder Homes</span></div>
    <div class="photo photo--green" role="img" aria-label="Caregiver hugging a smiling elderly woman in a wheelchair outdoors" style="left:0;top:66px;width:100%;height:400px;"></div>
    <svg class="curve" viewBox="0 0 247 575" preserveAspectRatio="none" aria-hidden="true">
      <path d="M0 440 C90 440 170 445 247 458 L247 575 L0 575 Z" fill="var(--sage)"/>
      <path d="M0 450 C90 458 170 462 247 478 L247 575 L0 575 Z" fill="var(--teal-dark)"/>
    </svg>
    <p class="center serif-line" style="top:487px;font-size:13px;line-height:1.45;color:var(--white);">We provide the love and care<br>needed to keep your loved ones<br>safely independent</p>
    <div class="center" style="top:545px;"><span class="url" style="display:inline-block;background:var(--pill);padding:0 14px;border-radius:10px;line-height:19px;">www.willowmerehomes.com</span></div>
  </article>
</section>

<!-- Inside spread -->
<section class="sheet sheet--inside" aria-label="Brochure inside">

  <article class="panel panel--services">
    <h2 class="heading heading--rule" style="left:14px;top:33px;">Our Services</h2>
    <p class="serif-line" style="left:14px;top:66px;width:220px;font-size:12px;line-height:1.2;color:var(--teal-text);">We provide the love and care needed to keep your loved ones safely independent.</p>
    <p style="left:14px;top:103px;width:220px;font-size:7px;line-height:1.3;">Whole-house generators to provide comforts and services to residents during unexpected weather or utility events.</p>
    <ul class="list" style="left:16px;top:134px;width:225px;">
      <li>24 Hours Care</li>
      <li>Assistance with Daily Living Activities</li>
      <li>Bathing Assistance</li>
      <li>Beauty and Haircare</li>
      <li>Laundry</li>
      <li>Linens</li>
      <li>Housekeeping</li>
      <li>3 Home-Cooked Meals and Snacks - Dietitian Approved</li>
      <li>Medication Reminders and Supervision</li>
      <li>Ambulatory Assistance and Supervision</li>
      <li>Other comforts One would have at One's home</li>
    </ul>
    <p class="serif-line" style="left:14px;top:325px;width:225px;font-size:12px;line-height:1.2;color:var(--teal-text);">We offer services that make daily living activities possible and safe, 24 hours a day!</p>
    <div class="photo photo--room" role="img" aria-label="Caregiver helping an elderly woman with a cane stand up" style="left:0;top:370px;width:100%;height:205px;"></div>
    <svg class="curve" viewBox="0 0 247 575" preserveAspectRatio="none" aria-hidden="true">
      <path d="M0 350 L247 350 L247 410 C200 375 120 362 0 378 Z" fill="var(--cream)"/>
      <path d="M0 370 C120 355 200 368 247 405 L247 416 C200 380 120 368 0 382 Z" fill="var(--taupe)"/>
    </svg>
  </article>

  <article class="panel panel--sage panel--rooms">
    <p class="center serif-line" style="top:55px;font-size:28px;letter-spacing:4px;color:#e4ece8;text-transform:uppercase;">Willowmere</p>
    <h2 class="center heading" style="top:138px;color:var(--teal-dark);font-size:22px;">Accommodation</h2>
    <p style="left:14px;top:186px;width:220px;font-size:7px;line-height:1.3;text-align:justify;color:var(--white);">From a shared room for those who enjoy the company to the private suit for those looking for more room, we have a wide variety of accommodations that meet everyone's personal preference.</p>
    <ul class="list" style="left:16px;top:244px;width:225px;">
      <li>Private or Shared Room</li>
      <li>Courtyard and Patio</li>
      <li>Kitchen</li>
      <li>Large Dining Room</li>
      <li>Large Family Room w/ Television for gathering</li>
      <li>Wheelchair Accessibility</li>
    </ul>
    <div class="photo photo--room photo--circle" role="img" aria-label="Caregiver making a bed" style="left:12px;top:355px;width:74px;height:74px;"></div>
    <div class="photo photo--room photo--circle" role="img" aria-label="Bright living room" style="left:87px;top:355px;width:74px;height:74px;"></div>
    <div class="photo photo--room photo--circle" role="img" aria-label="White kitchen" style="left:162px;top:355px;width:74px;height:74px;"></div>
    <p class="center" style="top:458px;padding:0 18px;font-size:7px;line-height:1.4;color:var(--white);">If you're looking for a place where your loved one can feel at home and receive the best care possible. We truly go above and beyond to provide a warm and compassionate space for our residents, and I have no doubt that your loved one would feel right at.</p>
    <div class="center" style="top:527px;">
      <span class="phone-pill"><svg viewBox="0 0 20 20" aria-hidden="true"><circle cx="10" cy="10" r="9.5" fill="#e9e6dc"/><circle cx="10" cy="10" r="7.5" fill="var(--teal-dark)"/><path d="M7 5.5 L8.6 5.3 L9.3 7.8 L8.2 8.6 C8.7 9.9 9.9 11.1 11.3 11.7 L12.1 10.6 L14.6 11.3 L14.4 12.9 C11 13.5 6.5 9 7 5.5 Z" fill="#fff"/></svg>(504) 555-0148</span>
    </div>
    <p class="center url" style="top:552px;color:var(--white);font-size:14px;">www.willowmerehomes.com</p>
  </article>

  <article class="panel panel--other">
    <div class="photo photo--warm" role="img" aria-label="Smiling caregiver holding hands with an elderly woman on a sofa" style="left:0;top:0;width:100%;height:230px;"></div>
    <svg class="curve" viewBox="0 0 247 575" preserveAspectRatio="none" aria-hidden="true">
      <path d="M0 225 C80 200 170 195 247 160 L247 575 L0 575 Z" fill="var(--cream)"/>
      <path d="M0 215 C80 192 170 185 247 150 L247 160 C170 195 80 205 0 232 Z" fill="var(--taupe)"/>
    </svg>
    <div class="photo photo--room photo--circle" role="img" aria-label="Caregiver's hand on an elderly person's shoulder" style="left:145px;top:134px;width:100px;height:100px;border:5px solid var(--taupe);"></div>
    <h2 class="heading" style="left:12px;top:244px;">Other Services</h2>
    <div class="service" style="top:280px;">
      <h3>Food Services</h3>
      <p>Three meals are provided on a daily basis as well as snacks during the day and before bedtime, if desired.</p>
      <p>Each meal is prepared in the kitchen by a staff member, and served in the dining room.</p>
      <p>Each meal can be modified to fit anyone's dietary needs.</p>
    </div>
    <div class="service" style="top:390px;">
      <h3>Laundry Services</h3>
      <p>Resident laundry is done by the staff. They wash, dry and fold and put away all clothes.</p>
    </div>
    <div class="service" style="top:440px;">
      <h3>Medication Storage</h3>
      <p>All medications are locked and stored. Staff members supervise medications.</p>
    </div>
    <div class="service" style="top:490px;">
      <h3>Safety</h3>
      <p>All locations are equipped with fire and security protection alarm systems that are monitored 24/7 and inspected annually.</p>
    </div>
    <p class="serif-line" style="left:10px;top:543px;width:224px;height:20px;line-height:20px;text-align:center;background:var(--taupe);color:var(--white);font-size:11.5px;border-radius:10px;">Family Owned and Operated Est. 2008</p>
  </article>
</section>

</body>
</html>
```